Copperkettle Menu

I want to re design my menu at our restaurant Copperkettle, the current menu and information about the restaurant is online at www.copperkettle-eatery.example.nz, have attached the logo for Copperkettle as well as the new menu specifications

Menu design Specifications
· Rustic

· Raw

· Unpolished

· Urban

```html
<!DOCTYPE html>
<html lang="en">
<head>
<meta charset="utf-8">
<title>Copperkettle Menu</title>
<link rel="stylesheet" href="https://fonts.googleapis.com/css2?family=Alfa+Slab+One&family=Josefin+Sans:wght@400;700&display=swap">
<style>
  :root {
    --kraft: #b99b7d;
    --kraft-light: #c2a487;
    --kraft-dark: #ad8f72;
    --ink: #8f3a22;
    --ink-soft: #9c4a30;
  }
  * { margin: 0; padding: 0; box-sizing: border-box; }
  html, body { width: 848px; height: 1200px; overflow: hidden; }
  body {
    position: relative;
    background: radial-gradient(ellipse at 40% 35%, var(--kraft-light), var(--kraft) 55%, var(--kraft-dark));
    color: var(--ink);
    font-family: "Josefin Sans", "Century Gothic", sans-serif;
  }
  .brand-name {
    position: absolute;
    left: 0; top: -14px;
    width: 848px;
    font-family: "Josefin Sans", sans-serif;
    font-weight: 700;
    font-size: 104px;
    line-height: 1;
    letter-spacing: -1px;
    color: var(--ink);
    white-space: nowrap;
    overflow: hidden;
    text-align: center;
  }
  .section { position: absolute; }
  .section-title {
    display: flex;
    justify-content: space-between;
    font-family: "Alfa Slab One", serif;
    font-weight: 400;
    font-size: 22px;
    letter-spacing: 1px;
    color: var(--ink);
  }
  .menu-list { list-style: none; }
  .menu-item {
    display: flex;
    align-items: baseline;
    height: 30px;
    line-height: 30px;
    font-size: 13.5px;
    letter-spacing: 0.6px;
    text-transform: uppercase;
    color: var(--ink-soft);
  }
  .menu-item .leader {
    flex: 1;
    margin: 0 2px;
    border-bottom: 1.5px dotted var(--ink-soft);
    transform: translateY(-3px);
  }
  .snacks { left: 33px; top: 137px; width: 397px; }
  .snacks .menu-list { margin-top: 24px; }
  .sweets { left: 493px; top: 133px; }
  .cheese { left: 493px; top: 353px; }
  .boards { left: 110px; top: 609px; width: 623px; }
  .boards .menu-list { margin-top: 31px; }
  .sides { left: 116px; top: 886px; width: 614px; }
  .sides .section-title { padding-right: 3px; }
  .sides .menu-list { margin-top: 58px; }
</style>
</head>
<body>
  <h1 class="brand-name">COPPERKETTLE</h1>

  <section class="section snacks">
    <h2 class="section-title">SNACKS</h2>
    <ul class="menu-list">
      <li class="menu-item"><span>Pork Crackling</span><span class="leader"></span><span>5</span></li>
      <li class="menu-item"><span>Venison Pasties &amp; Plum Sauce</span><span class="leader"></span><span>12</span></li>
      <li class="menu-item"><span>Lamb Meatballs &amp; Pomegranate Molasses</span><span class="leader"></span><span>15</span></li>
      <li class="menu-item"><span>Pulled Pork &amp; Apple Slaw Sliders</span><span class="leader"></span><span>12</span></li>
      <li class="menu-item"><span>Cheese Fondue and Asparagus</span><span class="leader"></span><span>10</span></li>
      <li class="menu-item"><span>Battered Fish Fingers &amp; Tartare Sauce</span><span class="leader"></span><span>9</span></li>
      <li class="menu-item"><span>Hand Cut Fries &amp; Tomato Sauce</span><span class="leader"></span><span>7</span></li>
      <li class="menu-item"><span>Salmon &amp; Avocado Filled Sesame Cones</span><span class="leader"></span><span>12</span></li>
      <li class="menu-item"><span>Parmesan, Chilly &amp; Lemon Skinny Fries</span><span class="leader"></span><span>7</span></li>
      <li class="menu-item"><span>Barbequed Chicken Tulips</span><span class="leader"></span><span>14</span></li>
      <li class="menu-item"><span>Steamed Mussles &amp; Tomato Salsa</span><span class="leader"></span><span>12</span></li>
      <li class="menu-item"><span>Garlic Bread</span><span class="leader"></span><span>6</span></li>
      <li class="menu-item"><span>Crispy Lentil Balls &amp; Roast Garlic Yogurt</span><span class="leader"></span><span>8</span></li>
    </ul>
  </section>

  <section class="section sweets">
    <h2 class="section-title">SWEETS</h2>
  </section>

  <section class="section cheese">
    <h2 class="section-title">CHEESE</h2>
  </section>

  <section class="section boards">
    <h2 class="section-title"><span>BOARDS+TWO SIDES</span><span>FOR 1/FOR 2</span></h2>
    <ul class="menu-list">
      <li class="menu-item"><span>Beef Wellington &amp; Red Wine Jus</span><span class="leader"></span><span>36/69</span></li>
      <li class="menu-item"><span>Apricot Glazed Chicken Crown</span><span class="leader"></span><span>34/45</span></li>
      <li class="menu-item"><span>Roast Pork Scotch &amp; Caramelized Apple Sauce</span><span class="leader"></span><span>32/60</span></li>
      <li class="menu-item"><span>Pan Fried Line Caught Fish &amp; Lemon Pickle</span><span class="leader"></span><span>35/67</span></li>
      <li class="menu-item"><span>Grilled Lamb Rack &amp; Mint Sauce</span><span class="leader"></span><span>38/72</span></li>
      <li class="menu-item"><span>Mixed Roast Nut Loaf &amp; Rhubarb Marmalade</span><span class="leader"></span><span>28/58</span></li>
    </ul>
  </section>

  <section class="section sides">
    <h2 class="section-title"><span>SALADS &amp; SIDES</span><span>SM/LG</span></h2>
    <ul class="menu-list">
      <li class="menu-item"><span>Warmed Red Skinnes Potatoeswith Dill &amp; Mustard</span><span class="leader"></span><span>7/9</span></li>
      <li class="menu-item"><span>Tomato &amp; Mixed Beans</span><span class="leader"></span><span>8/11</span></li>
      <li class="menu-item"><span>Char Grilled Vegetables &amp; Halloumi</span><span class="leader"></span><span>7/10</span></li>
      <li class="menu-item"><span>Orzo, Broadbean &amp; Feta</span><span class="leader"></span><span>7/10</span></li>
      <li class="menu-item"><span>Beetroot, Spinach &amp; Goat Cheese with Maple</span><span class="leader"></span><span>8/11</span></li>
      <li class="menu-item"><span>Mixed Leaves &amp; Citrus Emulsion</span><span class="leader"></span><span>6/9</span></li>
      <li class="menu-item"><span>Steamed Broccoli &amp; Sesame Butter</span><span class="leader"></span><span>6/9</span></li>
    </ul>
  </section>
</body>
</html>
```